Creating the Look and Feel of an Elite Boutique Consulting Practice: Vane Advisory

Complete a professional website on Weebly. As part of the site, we are open to a new logo -- we have just launched. We put up a starter website that shows you the content and theme we are going for. But clearly we aren't professional web designers and we need your help. Check out our start at vaneadvisory.com

Target Market(s)

Fortune 500 Clients

Industry/Entity Type

Management Consulting

Logo Text

VANE Advisory

Number of Pages Required

4 page

Requirements
Must have
• I've already set us up on Weebly. I'd like to give the selected designer the log-in credentials and have the designer create it on Weebly, so we can maintain it through that service.

```html
<!DOCTYPE html>
<html lang="en">
<head>
<meta charset="utf-8">
<title>Vane Advisory — Approach</title>
<link href="https://fonts.googleapis.com/css2?family=Open+Sans:wght@400;700&display=swap" rel="stylesheet">
<style>
  :root {
    --hero-dark: #0b1a1d;
    --hero-mid: #1d3236;
    --hero-light: #3a4d50;
    --white: #ffffff;
    --heading: #2e2e2e;
    --body-text: #5f5f5f;
    --rule: #dcdcdc;
    --accent: #2f8fe0;
  }
  * { box-sizing: border-box; margin: 0; padding: 0; }
  html, body { width: 1200px; height: 842px; overflow: hidden; background: var(--white); }
  body { font-family: "Open Sans", Arial, sans-serif; color: var(--heading); position: relative; }

  .hero {
    position: absolute; left: 0; top: 0; width: 1200px; height: 259px;
    background:
      radial-gradient(ellipse 260px 120px at 375px 260px, rgba(120,130,125,0.45), transparent 70%),
      radial-gradient(ellipse 420px 160px at 1000px 230px, rgba(90,105,100,0.35), transparent 70%),
      linear-gradient(180deg, var(--hero-dark) 0%, var(--hero-mid) 70%, var(--hero-light) 100%);
  }
  .site-header {
    position: absolute; left: 142px; top: 22px; width: 900px; height: 36px;
    display: flex; align-items: center; justify-content: space-between;
  }
  .brand { color: var(--white); font-size: 22px; font-weight: 400; letter-spacing: 0.2px; }
  .main-nav { display: flex; align-items: center; gap: 0; margin-right: -14px; }
  .main-nav a {
    color: var(--white); text-decoration: none; font-size: 13px; padding: 8px 20px;
  }
  .main-nav a.is-current {
    border: 2px solid var(--white); border-radius: 4px; padding: 8px 13px; margin-left: 8px;
  }
  .hero-title {
    position: absolute; left: 142px; top: 88px; width: 900px;
    text-align: center; color: var(--white);
    font-size: 37px; font-weight: 700; line-height: 45px; letter-spacing: 0.3px;
  }

  .approach { position: absolute; left: 142px; top: 290px; width: 900px; }
  .section-title {
    text-align: center; font-size: 30px; font-weight: 700; letter-spacing: 0.5px; line-height: 48px;
  }
  .section-rule { border: 0; border-top: 1px solid var(--rule); margin-top: 34px; }
  .columns { display: flex; justify-content: space-between; margin-top: 47px; }
  .column { width: 269px; text-align: center; }
  .column-image { width: 269px; height: 179px; display: block; }
  .img-desk { background: linear-gradient(135deg, #cfd8d6 0%, #6d7a72 45%, #2b2f33 100%); }
  .img-notes { background: linear-gradient(135deg, #3a3a36 0%, #d9d3a2 45%, #1c1c1c 100%); }
  .img-mouse { background: linear-gradient(160deg, #7f8483 0%, #c9c4c0 45%, #a7a7aa 100%); }
  .column-title { font-size: 17px; font-weight: 400; margin-top: 19px; line-height: 24px; }
  .column-text {
    font-size: 15px; line-height: 22.5px; color: var(--body-text); margin-top: 15px; padding: 0 3px;
  }
  .btn {
    display: inline-block; margin-top: 28px; width: 118px; height: 30px; line-height: 30px;
    background: var(--accent); color: var(--white); text-decoration: none;
    font-size: 13px; border-radius: 3px;
  }
</style>
</head>
<body>
  <section class="hero" role="img" aria-label="Dark teal city skyline with a domed cathedral and station roof">
  </section>
  <header class="site-header">
    <div class="brand">VANE ADVISORY</div>
    <nav class="main-nav">
      <a href="#">HOME</a>
      <a href="#">TEAM</a>
      <a href="#">CONTACT</a>
      <a href="#" class="is-current">APPROACH</a>
    </nav>
  </header>
  <h1 class="hero-title">LET'S WORK TOGETHER TO TRANSFORM YOUR ORGANIZATION</h1>

  <main class="approach">
    <h2 class="section-title">APPROACH</h2>
    <hr class="section-rule">
    <div class="columns">
      <article class="column">
        <div class="column-image img-desk" role="img" aria-label="Person writing in a notebook at a desk by a window"></div>
        <h3 class="column-title">APPROACH ONE</h3>
        <p class="column-text">Lorem ipsum dolor sit amet, consectetur adipisicing elit, sed do eiusmod tempor incididunt ut labore et dolore magna aliqua. Ut enim ad minim veniam.</p>
        <a href="#" class="btn">LEARN MORE</a>
      </article>
      <article class="column">
        <div class="column-image img-notes" role="img" aria-label="Yellow sticky notes with sketches on a dark table"></div>
        <h3 class="column-title">TWO</h3>
        <p class="column-text">Lorem ipsum dolor sit amet, consectetur adipisicing elit, sed do eiusmod tempor incididunt ut labore et dolore magna aliqua. Ut enim ad minim veniam.</p>
        <a href="#" class="btn">LEARN MORE</a>
      </article>
      <article class="column">
        <div class="column-image img-mouse" role="img" aria-label="Hand on a computer mouse beside a laptop"></div>
        <h3 class="column-title">APPROACH THREE</h3>
        <p class="column-text">Lorem ipsum dolor sit amet, consectetur adipisicing elit, sed do eiusmod tempor incididunt ut labore et dolore magna aliqua. Ut enim ad minim veniam.</p>
        <a href="#" class="btn">LEARN MORE</a>
      </article>
    </div>
  </main>
</body>
</html>
```